Iron Hoop Court Academy- Small Group and Private Lessons

I would like to advertise and drive my small group basketball lessons (offered on Fridays during the summer in Prosper, Texas with the following four groups- 1. Middle School Girls Small Group, 2. Middle School Boys Small Group, 3. High School Girls Small Group, 4. High School Boys Small Group).
Tag Line- "Do you want to become a complete player?"
We work to make each player as well rounded as possible by focusing on: balanced footwork, ballhandling, dribbling, finishing, passing, shooting, moving without the ball, basketball IQ
Website- www.ironhoopcourtacademy.com

```html
<!DOCTYPE html>
<html lang="en">
<head>
<meta charset="utf-8">
<title>Iron Hoop Court Academy – Small Group Lessons</title>
<link href="https://fonts.googleapis.com/css2?family=Oswald:wght@600;700&display=swap" rel="stylesheet">
<style>
  :root {
    --page: #f6f6f4;
    --wood-dark: #b8692c;
    --wood-mid: #cf8a45;
    --wood-light: #e2a65e;
    --court-line: rgba(255, 222, 130, 0.38);
    --ink: #ffffff;
    --shade: rgba(70, 30, 5, 0.55);
    --badge: #f07c12;
  }
  * { margin: 0; padding: 0; box-sizing: border-box; }
  html, body { width: 1200px; height: 1200px; overflow: hidden; background: var(--page); }
  .flyer {
    position: absolute; left: 136px; top: 0; width: 928px; height: 1200px;
    overflow: hidden;
    font-family: "Oswald", "Arial Narrow", sans-serif;
    color: var(--ink); text-transform: uppercase;
    text-shadow: 2px 3px 2px var(--shade);
  }
  .floor {
    position: absolute; inset: 0;
    background:
      radial-gradient(ellipse at 55% 45%, var(--wood-light) 0%, transparent 60%),
      linear-gradient(180deg, var(--wood-mid) 0%, var(--wood-dark) 100%);
  }
  .court-lines { position: absolute; inset: 0; }
  .headline { position: absolute; left: 90px; top: 62px; width: 412px; text-align: center; font-weight: 700; line-height: 1; white-space: nowrap; }
  .headline .lead { display: block; font-size: 60px; letter-spacing: 2px; margin-bottom: 10px; }
  .headline .big { display: block; font-size: 100px; letter-spacing: 3px; margin-top: 2px; }
  .brand { position: absolute; left: 600px; top: 50px; width: 224px; text-align: center; }
  .brand-mark { width: 176px; height: 176px; border-radius: 50%; background: var(--badge); margin: 0 auto 16px; box-shadow: 0 0 0 8px #fff; }
  .brand-name { font-size: 26px; font-weight: 700; line-height: 1.15; letter-spacing: 1px; }
  .skills { position: absolute; left: 110px; top: 386px; width: 708px; text-align: center; font-size: 32px; font-weight: 600; line-height: 43px; letter-spacing: 0.5px; }
  .lessons-title { position: absolute; left: 101px; top: 626px; width: 726px; text-align: center; font-size: 66px; font-weight: 700; letter-spacing: 2px; line-height: 1; white-space: nowrap; padding-bottom: 10px; border-bottom: 3px solid var(--ink); }
  .group { position: absolute; top: 738px; width: 380px; text-align: center; white-space: nowrap; }
  .group.middle { left: 70px; }
  .group.high { left: 494px; }
  .group .name { font-size: 33px; font-weight: 600; line-height: 44px; letter-spacing: 0.5px; }
  .price { margin-top: 18px; font-weight: 700; line-height: 1; }
  .price .amount { font-size: 78px; }
  .price .unit { font-size: 36px; }
  .cta { position: absolute; left: 0; top: 978px; width: 928px; text-align: center; font-size: 27px; font-weight: 600; line-height: 33px; letter-spacing: 0.5px; }
  .contact { position: absolute; left: 0; top: 1072px; width: 928px; text-align: center; font-size: 27px; font-weight: 600; line-height: 34px; letter-spacing: 0.5px; white-space: nowrap; }
</style>
</head>
<body>
<main class="flyer">
  <div class="floor" role="img" aria-label="Polished hardwood basketball court floor"></div>
  <svg class="court-lines" width="928" height="1200" viewBox="0 0 928 1200" aria-hidden="true">
    <circle cx="1184" cy="624" r="766" fill="none" stroke="var(--court-line)" stroke-width="22"/>
    <circle cx="1184" cy="624" r="690" fill="none" stroke="var(--court-line)" stroke-width="18"/>
  </svg>

  <h1 class="headline">
    <span class="lead">Do you want</span>
    <span class="lead">to become a</span>
    <span class="big">Player?</span>
  </h1>

  <div class="brand">
    <div class="brand-mark"></div>
    <p class="brand-name">Iron Hoop Court Academy</p>
  </div>

  <p class="skills">Want to improve your balanced footwork, ballhandling, dribbling, finishing, passing, shooting, moving without the ball, basketball IQ?</p>

  <h2 class="lessons-title">Small Group Lessons</h2>

  <section class="group middle">
    <p class="name">Middle School Boys</p>
    <p class="name">Middle School Girls</p>
    <p class="price"><span class="amount">$35</span><span class="unit">/hr</span></p>
  </section>

  <section class="group high">
    <p class="name">High School Boys</p>
    <p class="name">High School Girls</p>
    <p class="price"><span class="amount">$35</span><span class="unit">/hr</span></p>
  </section>

  <p class="cta">Ready to get better?<br>Contact me today!</p>

  <p class="contact">Email: info@ironhoopcourtacademy.com<br>Phone: 555-014-2760</p>
</main>
</body>
</html>
```